Dietary supplement, Clean and simple.

Hi,
I’d like to talk about the project,

About us:
We are a dietary supplement (Vitamins, Minerals, amino acids etc.) company.
The goal is to have about 25 products at the end of this year. However, for this goal to be achieved we need a good label design to make our products represent our company values.
I’ll be here every day supporting your questions, we are fully committed to making the highest/best quality/customer experience possible.

About the design and our values:
- Professional (We are in the industry of professionalism and expertise. I would love to show we are competent at this, Id. Like to have the labels looks like we have done our research.)
- Efficient (White spacing, good use of the space available.)
- Simple (Straight forward, in 5 seconds they have to know what the product they have is/how functions. We’re trying to simplify it for the consumer.
- No distractions (the only visually “distracting” factor can be the vector art.)

The guidelines:
The goal is to have a universal design, with one element that changes (Vector art). I’ll attach a file/multiple files I think can show some visuals on what I’m looking for, and what parts of the design I think are good/bad.

Label size: 69x155mm (Front is 77.5mm)

Design whatever you think fits our image. You’re the design expert, all I care about is that it fits our company standards/image.

Use this color/font.
Font: Sans Serif
Main company color is Mind green #237D62 (Use this color for something in the design.)

What I thought would be cool/might looks ugly, who knows:
1. The front of the label: Should have 1 vector art, preferably in the top right corner. (That looks good in multiple colors. The vector can have multiple areas to color, I would prefer 2 main colors in the vector art. The interchangeable colors are used for multiple kinds of products.)
2. Text/product information on the left. The text that will have to be displayed:
- Product name for instance “Magnesium + B6”
- Description for the product for instance “Magnesium with ginger taste”
- Company name or logo. (Add ® behind it. We are soon to be trademark registered.)
3. We need to show the "daily intake" amount on the front and also the amount in the complete bottle. For instance, “Daily intake 1 capsule, 60 capsules”.
• You don’t have to design the backside of the label. After I chose a design, I’d like to chat and give specific information on what areas need to be assigned where. (Too complex because of the law.)
Updates

Hi, Please make the deadline 31 days total. I want designers to have the time to design. And not be rushed to finish it.

I want to extend the deadline because i feel like a slightly more medical look would be interesting. Hope you can come up with something!!

Target Market(s)

Dietary supplement consumers

Industry/Entity Type

Dietary supplements

Font styles to use
Sans Serif

Colors

Requirements
Must have
• Trademark icon "®" has to be at the top right after the company logo(text of logo)/name.

```html
<!DOCTYPE html>
<html lang="en">
<head>
<meta charset="utf-8">
<title>Magnesium – Supplement Label</title>
<link href="https://fonts.googleapis.com/css2?family=Montserrat:wght@400;500;600;700;800&display=swap" rel="stylesheet">
<style>
  :root {
    --mind-green: #237D62;
    --leaf-green: #55a84f;
    --lime-light: #d6e593;
    --lime: #a8cf46;
    --lime-deep: #8fbd4c;
    --white: #ffffff;
  }
  html, body {
    margin: 0;
    padding: 0;
    width: 1200px;
    height: 535px;
    overflow: hidden;
    background: var(--white);
  }
  .label {
    position: relative;
    width: 1200px;
    height: 535px;
    font-family: "Montserrat", sans-serif;
  }
  .label__art {
    position: absolute;
    inset: 0;
    width: 1200px;
    height: 535px;
  }
  .brand {
    position: absolute;
    left: 650px;
    top: 58px;
    width: 160px;
    text-align: center;
    color: var(--mind-green);
    font-weight: 700;
  }
  .brand__dot {
    display: block;
    width: 26px;
    height: 26px;
    border-radius: 50%;
    background: var(--mind-green);
    margin: 0 auto 12px;
  }
  .brand__name {
    font-size: 22px;
    line-height: 1.05;
    letter-spacing: 1px;
  }
  .product {
    position: absolute;
    left: 403px;
    top: 211px;
    width: 420px;
    text-align: center;
  }
  .product__name {
    display: inline-block;
    margin: 0;
    padding: 0 4px;
    font-size: 52px;
    font-weight: 700;
    line-height: 1.05;
    white-space: nowrap;
    background: linear-gradient(90deg, #9cc83c 0%, #79b043 28%, #a9c956 55%, #d3e48c 72%, #8cbc3f 100%);
    -webkit-background-clip: text;
    background-clip: text;
    color: transparent;
  }
  .product__tagline {
    margin: 0 auto;
    height: 17px;
    width: 355px;
    border-radius: 9px;
    background: var(--leaf-green);
    color: var(--white);
    font-size: 16px;
    font-weight: 500;
    line-height: 17px;
    white-space: nowrap;
  }
  .intake {
    position: absolute;
    left: 717px;
    top: 0;
    width: 140px;
    height: 535px;
    text-align: center;
    pointer-events: none;
  }
  .intake span {
    position: absolute;
    left: 0;
    width: 140px;
    line-height: 1;
    white-space: nowrap;
  }
  .intake__note {
    top: 395px;
    color: var(--leaf-green);
    font-size: 12.5px;
    font-weight: 400;
  }
  .intake__dose {
    top: 409px;
    color: var(--leaf-green);
    font-size: 16px;
    font-weight: 700;
  }
  .intake__count {
    top: 436px;
    color: var(--white);
    font-size: 37px;
    font-weight: 800;
  }
  .intake__unit {
    top: 469px;
    color: var(--white);
    font-size: 12.5px;
    font-weight: 600;
  }
  .weight {
    position: absolute;
    left: 346px;
    top: 450px;
    width: 44px;
    height: 44px;
    border-radius: 50%;
    background: var(--white);
    color: var(--mind-green);
    text-align: center;
  }
  .weight__value {
    display: block;
    font-size: 15px;
    font-weight: 800;
    line-height: 1;
    margin-top: 11px;
  }
  .weight__unit {
    display: block;
    font-size: 7.5px;
    font-weight: 700;
    line-height: 1;
  }
</style>
</head>
<body>
<div class="label">
  <svg class="label__art" viewBox="0 0 1834 817" preserveAspectRatio="none" aria-hidden="true">
    <defs>
      <linearGradient id="band-gradient" x1="0" y1="0" x2="1" y2="0">
        <stop offset="0" stop-color="#d4e38f"/>
        <stop offset="0.25" stop-color="#aad04a"/>
        <stop offset="0.45" stop-color="#d6e593"/>
        <stop offset="0.55" stop-color="#93c04c"/>
        <stop offset="0.75" stop-color="#d7e694"/>
        <stop offset="1" stop-color="#a6cf45"/>
      </linearGradient>
      <linearGradient id="swoosh-gradient" x1="0" y1="0" x2="0" y2="1">
        <stop offset="0" stop-color="#c7dc6f"/>
        <stop offset="1" stop-color="#d2e389"/>
      </linearGradient>
      <linearGradient id="ring-gradient" x1="0" y1="0" x2="1" y2="1">
        <stop offset="0" stop-color="#f2f2f2"/>
        <stop offset="0.5" stop-color="#8d9090"/>
        <stop offset="1" stop-color="#e8e8e8"/>
      </linearGradient>
      <clipPath id="badge-lower">
        <rect x="1090" y="660" width="230" height="120"/>
      </clipPath>
    </defs>

    <rect class="top-band" x="458" y="0" width="915" height="27" fill="url(#band-gradient)"/>

    <path class="arc-right" d="M1130,27 L1210,27 C1330,90 1375,300 1307,495 C1330,330 1280,130 1130,27 Z" fill="url(#swoosh-gradient)"/>

    <path class="arc-left" d="M555,165 C480,330 480,560 695,695 C590,610 515,420 555,165 Z" fill="url(#swoosh-gradient)"/>

    <path class="base-wave" d="M452,360 C465,470 495,540 535,585 C590,645 640,685 695,695 C850,730 1050,726 1120,722 L1373,712 L1373,817 L452,817 Z" fill="url(#band-gradient)"/>

    <g class="intake-badge">
      <circle cx="1203" cy="662" r="102" fill="#c3dc63"/>
      <circle cx="1203" cy="662" r="92" fill="url(#ring-gradient)"/>
      <circle cx="1203" cy="662" r="87" fill="#ffffff"/>
      <circle cx="1203" cy="662" r="87" fill="#5aa84f" clip-path="url(#badge-lower)"/>
    </g>
  </svg>

  <div class="brand">
    <span class="brand__dot"></span>
    <div class="brand__name">VERDANT CALM®</div>
  </div>

  <div class="product">
    <h1 class="product__name">MAGNESIUM</h1>
    <p class="product__tagline">Magnesium with lemon taste</p>
  </div>

  <div class="intake">
    <span class="intake__note">take daily</span>
    <span class="intake__dose">1 CAPSULE</span>
    <span class="intake__count">60</span>
    <span class="intake__unit">capsules</span>
  </div>

  <div class="weight">
    <span class="weight__value">180</span>
    <span class="weight__unit">grams</span>
  </div>
</div>
</body>
</html>
```